Tolvek Consulting
Tolvek Consulting stationary
Tolvek Consulting - Consulting
Creative Brief
Professional
Daniel R. Tolvek
Chief Executive Officer
Tolvek Consulting, LLC P.O. Box 4372 Phoenix, AZ 85004
daniel@danielrtolvek-mail.com
danielrtolvek-mail.com
Tolvek Consulting Logo

```html
<!DOCTYPE html>
<html lang="en">
<head>
<meta charset="utf-8">
<title>Tolvek Consulting — Stationery</title>
<link href="https://fonts.googleapis.com/css2?family=Montserrat:wght@600;700&family=Open+Sans:wght@400;600&display=swap" rel="stylesheet">
<style>
  :root{
    --bg:#2a2a2c;
    --paper:#ffffff;
    --ink:#3a3a3a;
    --muted:#8a8a8a;
    --rule:#d9d9d9;
    --brand-blue:#1a76c2;
    --brand-navy:#0b3b78;
    --brand-cyan:#39b6e6;
    --brand-orange:#f39200;
    --brand-orange-dark:#e0561b;
  }
  *{box-sizing:border-box;margin:0;padding:0}
  html,body{width:1200px;height:888px;overflow:hidden}
  body{background:var(--bg);font-family:"Open Sans",sans-serif;color:var(--ink);position:relative}

  .sheet{position:absolute;background:var(--paper);overflow:hidden;box-shadow:0 6px 18px rgba(0,0,0,.35)}
  .brand{display:flex;align-items:center;gap:7px}
  .brand-dot{width:16px;height:16px;border-radius:50%;background:var(--brand-orange);flex:none}
  .brand-name{font-family:"Montserrat",sans-serif;font-weight:700;font-size:14px;color:var(--brand-navy);letter-spacing:.02em;line-height:1.1}
  .small{font-size:8px;line-height:1.5;color:var(--muted)}
  .accent-band{position:absolute;left:0;right:0;bottom:0;height:6px;background:linear-gradient(90deg,var(--brand-navy),var(--brand-blue) 40%,var(--brand-cyan))}

  /* Letterhead */
  .letterhead{left:40px;top:50px;width:340px;height:480px;padding:28px 28px}
  .letterhead .contact{position:absolute;right:28px;top:30px;text-align:right}
  .letterhead .body{margin-top:70px;font-size:8px;line-height:1.7;color:var(--ink)}
  .letterhead .body p{margin-bottom:10px}
  .signature{margin-top:26px;width:90px;height:26px}
  .signature-name{font-size:8px;font-weight:600;color:var(--ink)}

  /* Fax */
  .fax{left:410px;top:50px;width:340px;height:480px;padding:28px}
  .fax .title{position:absolute;right:28px;top:28px;font-family:"Montserrat",sans-serif;font-weight:700;font-size:22px;color:var(--brand-navy);letter-spacing:.12em}
  .fax .contact{margin-top:10px}
  .fax-table{margin-top:34px;width:100%;border-collapse:collapse;font-size:8px}
  .fax-table th{width:60px;text-align:left;background:#eceff3;color:var(--brand-navy);font-weight:600;padding:7px 8px;border-bottom:2px solid #fff}
  .fax-table td{border-bottom:1px solid var(--rule)}
  .fax-checks{display:flex;gap:22px;margin-top:20px;font-size:8px;color:var(--ink)}
  .fax-checks span::before{content:"";display:inline-block;width:8px;height:8px;border:1px solid var(--muted);margin-right:5px;vertical-align:-1px}
  .fax-lines{margin-top:26px}
  .fax-lines div{height:1px;background:var(--rule);margin-bottom:18px}

  /* Business cards */
  .card{width:350px;height:200px}
  .card-front{left:790px;top:50px;padding:24px}
  .card-front .person{position:absolute;right:24px;top:26px;text-align:right}
  .person-name{font-family:"Montserrat",sans-serif;font-weight:700;font-size:13px;color:var(--brand-orange-dark)}
  .person-title{font-size:8px;color:var(--muted);margin-top:2px}
  .card-front .details{position:absolute;left:24px;bottom:26px}
  .card-front .details li{list-style:none;display:flex;align-items:center;gap:6px}
  .card-front .details svg{width:9px;height:9px;fill:var(--brand-orange)}
  .card-back{left:790px;top:280px;background:linear-gradient(135deg,var(--brand-navy) 0%,var(--brand-blue) 38%,var(--brand-orange) 62%,var(--brand-orange-dark) 100%);display:flex;align-items:center;justify-content:center}
  .card-back .brand-name{color:#fff;font-size:18px}
  .card-back .brand-dot{background:#fff;width:20px;height:20px}

  /* Envelope */
  .envelope{left:40px;top:570px;width:560px;height:280px;padding:26px}
  .envelope .flap{position:absolute;left:0;top:0;width:220px;height:280px}
  .envelope .brand,.envelope .return{position:relative}
  .envelope .brand-name{color:#fff}
  .envelope .brand-dot{background:#fff}
  .envelope .return{margin-top:8px;color:#cfe3f5;width:170px}
  .envelope .window{position:absolute;left:300px;top:130px;width:220px;height:70px;border:1px solid var(--rule);border-radius:3px}

  /* Compliment slip */
  .slip{left:640px;top:530px;width:500px;height:320px;padding:30px}
  .slip .contact{position:absolute;right:30px;top:32px;text-align:right}
  .slip .note{position:absolute;left:30px;top:140px;font-family:"Montserrat",sans-serif;font-weight:600;font-size:16px;color:var(--brand-blue)}
</style>
</head>
<body>

<section class="sheet letterhead" aria-label="Letterhead">
  <div class="brand"><span class="brand-dot"></span><span class="brand-name">Tolvek Consulting</span></div>
  <div class="contact small">Tolvek Consulting, LLC<br>P.O. Box 4372 Phoenix, AZ 85004<br>daniel@danielrtolvek-mail.com<br>danielrtolvek-mail.com</div>
  <div class="body">
    <p>Dear Client,</p>
    <p>Thank you for choosing us. We look forward to working with you on your next project.</p>
    <p>Please find the proposal attached for your review.</p>
    <p>Sincerely,</p>
  </div>
  <svg class="signature" viewBox="0 0 90 26" aria-hidden="true"><path d="M4 20c8-14 14-16 14-6s8 6 14-4 6 10 14 4 16-8 40-6" fill="none" stroke="#333" stroke-width="1.2"/></svg>
  <div class="signature-name">Daniel R. Tolvek</div>
  <div class="accent-band"></div>
</section>

<section class="sheet fax" aria-label="Fax cover sheet">
  <div class="brand"><span class="brand-dot"></span><span class="brand-name">Tolvek Consulting</span></div>
  <div class="title">FAX</div>
  <div class="contact small">P.O. Box 4372 Phoenix, AZ 85004 · danielrtolvek-mail.com</div>
  <table class="fax-table">
    <tr><th>To</th><td></td></tr>
    <tr><th>From</th><td></td></tr>
    <tr><th>Date</th><td></td></tr>
    <tr><th>Pages</th><td></td></tr>
    <tr><th>Re</th><td></td></tr>
  </table>
  <div class="fax-checks"><span>Urgent</span><span>Review</span><span>Reply</span></div>
  <div class="fax-lines"><div></div><div></div><div></div><div></div><div></div><div></div></div>
  <div class="accent-band"></div>
</section>

<section class="sheet card card-front" aria-label="Business card front">
  <div class="brand"><span class="brand-dot"></span><span class="brand-name">Tolvek Consulting</span></div>
  <div class="person">
    <div class="person-name">Daniel R. Tolvek</div>
    <div class="person-title">Chief Executive Officer</div>
  </div>
  <ul class="details small">
    <li><svg viewBox="0 0 10 10"><path d="M5 0a3.5 3.5 0 0 0-3.5 3.5C1.5 6 5 10 5 10s3.5-4 3.5-6.5A3.5 3.5 0 0 0 5 0zm0 5a1.5 1.5 0 1 1 0-3 1.5 1.5 0 0 1 0 3z"/></svg>Tolvek Consulting, LLC · P.O. Box 4372 Phoenix, AZ 85004</li>
    <li><svg viewBox="0 0 10 10"><path d="M0 2h10v6H0zM0 2l5 3.5L10 2" /></svg>daniel@danielrtolvek-mail.com</li>
    <li><svg viewBox="0 0 10 10"><circle cx="5" cy="5" r="4.5"/></svg>danielrtolvek-mail.com</li>
  </ul>
  <div class="accent-band"></div>
</section>

<section class="sheet card card-back" aria-label="Business card back">
  <div class="brand"><span class="brand-dot"></span><span class="brand-name">Tolvek Consulting</span></div>
</section>

<section class="sheet envelope" aria-label="Envelope">
  <svg class="flap" viewBox="0 0 220 280" preserveAspectRatio="none" aria-hidden="true">
    <defs><linearGradient id="flapFill" x1="0" y1="0" x2="1" y2="1"><stop offset="0" stop-color="#0b3b78"/><stop offset="1" stop-color="#1a76c2"/></linearGradient></defs>
    <path d="M0 0H170C220 90 220 190 170 280H0Z" fill="url(#flapFill)"/>
  </svg>
  <div class="brand"><span class="brand-dot"></span><span class="brand-name">Tolvek Consulting</span></div>
  <div class="return small">Tolvek Consulting, LLC<br>P.O. Box 4372 Phoenix, AZ 85004</div>
  <div class="window"></div>
</section>

<section class="sheet slip" aria-label="Compliment slip">
  <div class="brand"><span class="brand-dot"></span><span class="brand-name">Tolvek Consulting</span></div>
  <div class="contact small">Tolvek Consulting, LLC<br>P.O. Box 4372 Phoenix, AZ 85004<br>daniel@danielrtolvek-mail.com<br>danielrtolvek-mail.com</div>
  <div class="note">With compliments</div>
  <div class="accent-band"></div>
</section>

</body>
</html>
```